Clinical Hypnotherapy

I need a flyer to promote my services as a highly qualified Clinical Hypnotherapist . This flyer will be distributed at various alternative health clinic where I see clients and should explain to the client what hypnotherapy is and how it can help them . I would like it to match my website ( www.brenwickcalm.co.uk ) as closely as possible in terms of the images , fonts and colours used . For this reason I include the following information that was supplied by the web designers :
Image : www.pixavane.com - photo no. 4817265
Fonts in banner : Avenir Next Condensed , Arial Narrow
Main colour used for background : #0b3166
Attached is a file with text . Depending on available space I can provide additional text or if neccesary remove text .
Kindly also inform me of the cost prior to going ahead
Updates
Thank you for designs submitted so far . My fault but I realise that I originally included way too much text in my brief . Please find new attachment with reduced text . This will hopefully allow for a more eye catching less cluttered design . I would also like to have a logo designed for Brenwick Calm - something abstract which reflects the psychotherapeutic / mind nature of the therapy .
Industry/Entity Type
Hypnotherapy
Look and feel
Each slider illustrates characteristics of the customer's brand and the style your logo design should communicate.

```html
<!DOCTYPE html>
<html lang="en">
<head>
<meta charset="utf-8">
<title>Brenwick Calm – Clinical Hypnotherapy</title>
<link rel="stylesheet" href="https://fonts.googleapis.com/css2?family=Arimo:wght@400;700&family=Roboto+Condensed:wght@300;400;700&display=swap">
<style>
  :root {
    --navy: #0b3166;
    --blue: #1f6fb8;
    --sky: #3fa9e0;
    --pale: #a9d6f2;
    --ink: #3a3a3a;
    --white: #ffffff;
    --rule: #b5b5b5;
  }
  * { box-sizing: border-box; margin: 0; padding: 0; }
  html, body { width: 850px; height: 1200px; overflow: hidden; background: var(--white); }
  .flyer { position: relative; width: 850px; height: 1200px; overflow: hidden; font-family: "Arimo", Arial, sans-serif; color: var(--ink); }
  .backdrop { position: absolute; inset: 0; }

  .brand { position: absolute; top: 72px; left: 316px; display: flex; align-items: center; gap: 16px; }
  .brand-mark { width: 70px; height: 70px; border-radius: 50%; border: 5px solid var(--blue); flex: none; }
  .brand-name { font-family: "Arimo", Arial, sans-serif; font-size: 43px; font-weight: 400; color: var(--blue); letter-spacing: -0.5px; line-height: 1; margin-top: 6px; }

  .portrait { position: absolute; left: 0; top: 178px; width: 352px; height: 480px;
    background: linear-gradient(180deg, #6c6660 0%, #4e4a48 30%, #2c2f36 65%, #1c1f26 100%);
    clip-path: path("M0 120 C20 40 90 0 180 0 C270 0 300 60 300 150 L310 300 C330 320 352 330 352 340 L352 380 C250 420 120 450 0 480 Z"); }

  .quote { position: absolute; top: 262px; left: 350px; width: 440px; text-align: center; color: var(--white); font-family: "Roboto Condensed", "Arial Narrow", sans-serif; }
  .quote-mark { font-size: 34px; line-height: 20px; color: rgba(255,255,255,0.45); font-family: Georgia, serif; }
  .quote-text { font-size: 27.5px; font-weight: 400; line-height: 33.5px; margin: 6px 0 0; letter-spacing: -0.2px; }
  .quote-mark.close { margin-top: 10px; }
  .credit { margin-top: 10px; font-family: "Arimo", Arial, sans-serif; font-weight: 700; font-size: 18.5px; line-height: 26px; }

  .column { position: absolute; top: 664px; }
  .column.general { left: 56px; width: 330px; }
  .column.clinical { left: 424px; width: 400px; }
  .divider { position: absolute; left: 397px; top: 664px; height: 376px; border-left: 2px dotted var(--rule); }
  .column h2 { font-weight: 400; font-size: 27px; line-height: 33px; color: var(--ink); }
  .column h2 .accent { color: var(--blue); }
  .service-list { list-style: none; margin-top: 38px; font-size: 17px; line-height: 21px; color: var(--ink); }
  .service-list li { position: relative; padding-left: 16px; margin-bottom: 13px; }
  .service-list li::before { content: ""; position: absolute; left: 2px; top: 5px; width: 7px; height: 7px; border-radius: 50%; background: var(--sky); }
  .service-grid { display: grid; grid-template-columns: 186px 200px; column-gap: 0; }
  .service-grid li { margin-bottom: 13.2px; }

  .footer { position: absolute; left: 0; top: 1095px; width: 850px; height: 47px;
    background: linear-gradient(90deg, var(--sky) 0%, #2a7fc6 55%, var(--navy) 100%);
    display: flex; align-items: center; justify-content: space-between; padding: 0 62px 0 57px; color: var(--white); font-size: 17px; }
  .contact { display: flex; align-items: center; gap: 12px; }
</style>
</head>
<body>
<main class="flyer">
  <svg class="backdrop" width="850" height="1200" viewBox="0 0 850 1200" aria-hidden="true">
    <defs>
      <linearGradient id="bandFill" x1="0" y1="0" x2="1" y2="0">
        <stop offset="0" stop-color="#3fa9e0"/>
        <stop offset="0.45" stop-color="#2b86cc"/>
        <stop offset="1" stop-color="#0b3166"/>
      </linearGradient>
      <linearGradient id="paleFill" x1="0" y1="0" x2="1" y2="0">
        <stop offset="0" stop-color="#a9d6f2"/>
        <stop offset="1" stop-color="#3fa9e0"/>
      </linearGradient>
    </defs>
    <path d="M0 60 C200 110 420 150 850 100 L850 720 L0 720 Z" fill="url(#bandFill)"/>
    <path d="M0 95 C180 150 360 190 520 200 C660 205 780 170 850 120 L850 150 C740 220 580 250 420 240 C260 228 110 170 0 130 Z" fill="url(#paleFill)" opacity="0.85"/>
    <path d="M0 0 L850 0 L850 120 C760 190 620 240 440 245 C280 242 120 175 0 122 Z" fill="#ffffff"/>
    <path d="M0 650 C120 590 300 535 460 525 C610 520 750 570 850 640 L850 1200 L0 1200 Z" fill="url(#paleFill)"/>
    <path d="M0 662 C140 600 320 550 470 545 C620 542 760 620 850 720 L850 1200 L0 1200 Z" fill="#ffffff"/>
  </svg>

  <div class="brand">
    <span class="brand-mark"></span>
    <span class="brand-name">Brenwick Calm</span>
  </div>

  <div class="portrait" role="img" aria-label="Portrait photograph of the hypnotherapist in a dark suit and tie"></div>

  <blockquote class="quote">
    <div class="quote-mark">&ldquo;</div>
    <p class="quote-text">Are YOU struggling with problems<br>made worse by STRESS and ANXIETY<br>or do you need to make<br>a REAL CHANGE in your life?</p>
    <div class="quote-mark close">&rdquo;</div>
    <p class="credit">Daniel Harcourt,<br>MSc (Clin.Hyp.) AdvHyp. DipCBHyp, Registered</p>
  </blockquote>

  <section class="column general">
    <h2><span class="accent">Hypnosis</span><br>Can Help With...</h2>
    <ul class="service-list">
      <li>Stress Management</li>
      <li>Resolving emotional blocks</li>
      <li>Adapting unhelpful beliefs and<br>behaviours to become beneficial ones</li>
      <li>Developing greater self-esteem</li>
      <li>Creating emotional and<br>practical resources</li>
      <li>Establishing positive new<br>goals for the future</li>
    </ul>
  </section>

  <div class="divider"></div>

  <section class="column clinical">
    <h2>Clinical <span class="accent">Hypnotherapy</span><br>Can Help You With...</h2>
    <ul class="service-list service-grid">
      <li>Weight Control</li><li>Performance Anxiety</li>
      <li>Binge Eating</li><li>Panic Attacks</li>
      <li>Virtual Gastric Band</li><li>Managing Stress</li>
      <li>Low Self Esteem</li><li>Phobias</li>
      <li>Depression</li><li>Sleep Problems</li>
      <li>Addiction</li><li>Pain Management</li>
      <li>Stop Smoking</li><li>Cancer Support</li>
    </ul>
  </section>

  <footer class="footer">
    <span class="locations">Ashcombe &nbsp;|&nbsp; Fern Vale &nbsp;|&nbsp; Kingsmere</span>
    <span class="contact">
      <svg width="20" height="32" viewBox="0 0 20 32" aria-hidden="true">
        <rect x="1.5" y="1.5" width="17" height="29" rx="3" fill="none" stroke="#ffffff" stroke-width="2.5"/>
        <line x1="2" y1="25" x2="18" y2="25" stroke="#ffffff" stroke-width="2"/>
      </svg>
      075 1842 6637
    </span>
  </footer>
</main>
</body>
</html>
```